Need a plumber

Would like a postcard sized flyer made up. Want the design to be kept very simple.
List of services we carry out in bullet point or similar.
Phone number and email included on the flyer.
Logo to feature prominantly.

List of services: Hot water issues
Burst Pipes
Gas Plumbing
Roof leaks
Drain blockages

Target Market(s)

Mums, dads and hosehgold owners

Industry/Entity Type

Plumbing

Colors
0054AA
0677BA
7BADD7
CADEEF
E8F1F8

Requirements
Must have
• Services we off and our logo, also must say "local plumber"

```html
<!DOCTYPE html>
<html lang="en">
<head>
<meta charset="utf-8">
<title>Need A Plumber? – Clearline Plumbing Flyer</title>
<link rel="stylesheet" href="https://fonts.googleapis.com/css2?family=Montserrat:wght@700&family=Barlow+Condensed:wght@500;600&display=swap">
<style>
  :root {
    --page-bg: #d9e9f9;
    --navy: #1b2358;
    --navy-deep: #10163f;
    --pill-navy: #1f2a62;
    --sky: #29a3e0;
    --sky-line: #3aa8e4;
    --white: #ffffff;
    --ink: #1a1a1a;
    --chrome-bright: #e6e6e6;
    --steel-light: #bdbdbd;
    --steel-mid: #8a8a8a;
    --steel-dark: #4a4a4a;
    --steel-shadow: #2e2e2e;
  }
  * { box-sizing: border-box; margin: 0; padding: 0; }
  html, body {
    width: 1200px; height: 1200px; overflow: hidden;
    background: var(--page-bg);
  }
  .flyer {
    position: absolute; left: 50px; top: 244px;
    width: 1100px; height: 712px; overflow: hidden;
    font-family: "Barlow Condensed", sans-serif;
  }
  .flyer__backdrop {
    position: absolute; inset: 0;
    background: radial-gradient(ellipse at 85% 30%, #2a3577 0%, var(--navy) 45%, var(--navy-deep) 100%);
  }
  .flyer__lens { position: absolute; inset: 0; }
  .brand-badge {
    position: absolute; left: 68px; top: 67px;
    width: 180px; height: 180px; border-radius: 50%;
    background: var(--white);
    border: 3px solid var(--ink);
    box-shadow: inset 0 0 0 5px var(--white), inset 0 0 0 7px var(--sky);
    display: flex; align-items: center; justify-content: center;
    text-align: center;
  }
  .brand-badge__name {
    font-family: "Barlow Condensed", sans-serif; font-weight: 600;
    color: var(--ink); font-size: 25px; letter-spacing: 4px; line-height: 1.15;
  }
  .headline {
    position: absolute; left: 0; width: 1100px; top: 86px;
    text-align: center; font-family: "Montserrat", sans-serif; font-weight: 700;
    color: var(--white); font-size: 92px; line-height: 80px; letter-spacing: -1px;
    text-shadow: 0 2px 10px rgba(0,0,0,0.3);
  }
  .headline span { display: block; }
  .tagline {
    position: absolute; left: 0; width: 1100px; top: 270px;
    text-align: center; color: var(--white);
    font-size: 30px; font-weight: 600; letter-spacing: 6px; text-transform: uppercase;
    text-shadow: 0 1px 6px rgba(0,0,0,0.45);
  }
  .services {
    position: absolute; left: 0; top: 390px; width: 1100px; height: 200px; list-style: none;
  }
  .service {
    position: absolute; top: 0; width: 150px; margin-left: -75px; text-align: center;
  }
  .service__icon { display: block; margin: 0 auto; width: 122px; height: 122px; }
  .service__label {
    display: block; margin-top: 8px;
    color: var(--white); font-size: 21px; font-weight: 500; line-height: 27px;
    text-transform: uppercase;
    text-shadow: 0 1px 4px rgba(0,0,0,0.45);
  }
  .contact {
    position: absolute; top: 625px; height: 52px;
    background: var(--pill-navy); border: 2px solid var(--white); border-radius: 10px;
    color: var(--sky); display: flex; align-items: center; justify-content: center;
  }
  .contact--phone { left: 271px; width: 251px; font-size: 28px; font-weight: 600; letter-spacing: 1.5px; gap: 22px; }
  .contact--email { left: 573px; width: 251px; font-size: 17px; font-weight: 500; }
  .contact__icon { width: 32px; height: 32px; }
</style>
</head>
<body>
  <main class="flyer">
    <div class="flyer__backdrop" role="img" aria-label="Dark blue toned photo of a plumber's hands at work"></div>

    <svg class="flyer__lens" viewBox="0 0 1100 712" role="img" aria-label="Black and white close-up photo of a wrench tightening a chrome pipe fitting">
      <defs>
        <clipPath id="lens-clip"><circle cx="550" cy="340" r="450"/></clipPath>
        <linearGradient id="lens-base" x1="0" y1="0" x2="1" y2="0">
          <stop offset="0" stop-color="var(--steel-dark)"/>
          <stop offset="0.3" stop-color="var(--steel-mid)"/>
          <stop offset="0.5" stop-color="var(--steel-light)"/>
          <stop offset="0.75" stop-color="var(--steel-mid)"/>
          <stop offset="1" stop-color="var(--steel-dark)"/>
        </linearGradient>
        <linearGradient id="lens-pipe" x1="0" y1="0" x2="1" y2="0">
          <stop offset="0" stop-color="var(--steel-mid)" stop-opacity="0"/>
          <stop offset="0.35" stop-color="var(--chrome-bright)" stop-opacity="0.8"/>
          <stop offset="0.55" stop-color="var(--steel-dark)" stop-opacity="0.5"/>
          <stop offset="0.8" stop-color="var(--chrome-bright)" stop-opacity="0.6"/>
          <stop offset="1" stop-color="var(--steel-mid)" stop-opacity="0"/>
        </linearGradient>
        <linearGradient id="lens-band" x1="0" y1="0" x2="0" y2="1">
          <stop offset="0" stop-color="var(--steel-shadow)" stop-opacity="0"/>
          <stop offset="0.5" stop-color="var(--steel-shadow)" stop-opacity="0.45"/>
          <stop offset="1" stop-color="var(--steel-shadow)" stop-opacity="0"/>
        </linearGradient>
        <radialGradient id="lens-glow" cx="0.82" cy="0.45" r="0.3">
          <stop offset="0" stop-color="var(--chrome-bright)" stop-opacity="0.55"/>
          <stop offset="1" stop-color="var(--chrome-bright)" stop-opacity="0"/>
        </radialGradient>
      </defs>
      <circle cx="550" cy="340" r="456" fill="none" stroke="var(--white)" stroke-width="2"/>
      <g clip-path="url(#lens-clip)">
        <rect x="0" y="0" width="1100" height="712" fill="url(#lens-base)"/>
        <rect x="470" y="0" width="170" height="712" fill="url(#lens-pipe)"/>
        <rect x="0" y="0" width="1100" height="712" fill="url(#lens-glow)"/>
        <rect x="100" y="300" width="720" height="150" fill="url(#lens-band)" transform="rotate(-4 460 375)"/>
      </g>
      <circle cx="550" cy="340" r="450" fill="none" stroke="var(--sky-line)" stroke-width="3"/>
    </svg>

    <div class="brand-badge">
      <span class="brand-badge__name">CLEARLINE<br>PLUMBING</span>
    </div>

    <h1 class="headline"><span>Need</span><span>A Plumber?</span></h1>
    <p class="tagline">Your Local Plumber</p>

    <ul class="services">
      <li class="service" style="left:244px">
        <svg class="service__icon" viewBox="0 0 122 122" aria-hidden="true">
          <circle cx="61" cy="61" r="59" fill="var(--sky)" stroke="var(--white)" stroke-width="2"/>
          <g fill="none" stroke="var(--pill-navy)" stroke-width="3" stroke-linecap="round">
            <path d="M64 36v30a9 9 0 1 0 10 0V36a5 5 0 0 0-10 0z"/>
            <circle cx="69" cy="74" r="4"/>
            <path d="M40 44c3-3-3-6 0-9M48 44c3-3-3-6 0-9M56 44c3-3-3-6 0-9"/>
            <path d="M38 54h20M38 62h20"/>
            <circle cx="44" cy="76" r="3"/><circle cx="52" cy="70" r="2"/>
          </g>
        </svg>
        <span class="service__label">Hot Water<br>Issues</span>
      </li>
      <li class="service" style="left:396px">
        <svg class="service__icon" viewBox="0 0 122 122" aria-hidden="true">
          <circle cx="61" cy="61" r="59" fill="var(--sky)" stroke="var(--white)" stroke-width="2"/>
          <g fill="none" stroke="var(--pill-navy)" stroke-width="3" stroke-linejoin="round">
            <rect x="30" y="58" width="62" height="24" rx="3"/>
            <path d="M38 58v24M84 58v24"/>
            <path d="M56 58l6 10-6 6 6 8"/>
            <path d="M40 52c0-12 10-18 21-10 11-8 21-2 21 10"/>
          </g>
        </svg>
        <span class="service__label">Burst<br>Pipes</span>
      </li>
      <li class="service" style="left:550px">
        <svg class="service__icon" viewBox="0 0 122 122" aria-hidden="true">
          <circle cx="61" cy="61" r="59" fill="var(--sky)" stroke="var(--white)" stroke-width="2"/>
          <g fill="none" stroke="var(--pill-navy)" stroke-width="3" stroke-linecap="round">
            <path d="M52 38h18M61 38v10"/>
            <rect x="50" y="48" width="22" height="28" rx="3"/>
            <path d="M34 58h16M34 68h16M72 58h16M72 68h16M34 56v14M88 56v14"/>
          </g>
        </svg>
        <span class="service__label">Gas<br>Plumbing</span>
      </li>
      <li class="service" style="left:703px">
        <svg class="service__icon" viewBox="0 0 122 122" aria-hidden="true">
          <circle cx="61" cy="61" r="59" fill="var(--sky)" stroke="var(--white)" stroke-width="2"/>
          <g fill="none" stroke="var(--pill-navy)" stroke-width="3" stroke-linejoin="round">
            <path d="M38 38h46v10H38z"/>
            <path d="M42 48v36M80 48v36M48 48l8 16h10l8-16"/>
            <path d="M61 64v6m-4 6a4 4 0 0 0 8 0l-4-6z"/>
          </g>
        </svg>
        <span class="service__label">Roof<br>Leaks</span>
      </li>
      <li class="service" style="left:855px">
        <svg class="service__icon" viewBox="0 0 122 122" aria-hidden="true">
          <circle cx="61" cy="61" r="59" fill="var(--sky)" stroke="var(--white)" stroke-width="2"/>
          <g fill="none" stroke="var(--pill-navy)" stroke-width="3" stroke-linecap="round">
            <path d="M36 56v12a12 12 0 0 0 24 0V48a10 10 0 0 1 20 0v8"/>
            <path d="M44 56v12a4 4 0 0 0 8 0V48a18 18 0 0 1 36 0v8"/>
            <path d="M32 56h16M76 56h16"/>
          </g>
        </svg>
        <span class="service__label">Drain<br>Blockages</span>
      </li>
    </ul>

    <div class="contact contact--phone">
      <svg class="contact__icon" viewBox="0 0 32 32" aria-hidden="true">
        <path d="M9 4l4 6-3 3c1.5 3.5 4.5 6.5 8 8l3-3 6 4-2 5c-10 1-21-10-20-20z" fill="none" stroke="var(--sky)" stroke-width="2" stroke-linejoin="round"/>
        <path d="M19 5a9 9 0 0 1 8 8M19 10a4 4 0 0 1 3 3" fill="none" stroke="var(--sky)" stroke-width="2" stroke-linecap="round"/>
      </svg>
      <span>0400 123 987</span>
    </div>
    <div class="contact contact--email">hello@clearlineplumbing.com.au</div>
  </main>
</body>
</html>
```